buseisness card

design a card that similar to my web site
BRIXENTAPLORLLC .COM

Contact Information for Business Card

NAME PHONE # WEBSITE EMAIL AND DISCTIPTION OF WHAT WE DO

Colors
0054AA
0677BA
7BADD7
CADEEF
E8F1F8

Requirements
Must have
• lOGO AND DETAILS
Nice to have
• I LIKE THE WATER LIKE ON MY WEB SITE

```html
<!DOCTYPE html>
<html lang="en">
<head>
<meta charset="utf-8">
<title>Brixen Taplor – Business Card</title>
<link rel="stylesheet" href="https://fonts.googleapis.com/css2?family=Montserrat:wght@600;700&family=Roboto:wght@400;500&display=swap">
<style>
  :root {
    --backdrop: #8f9092;
    --brand-blue: #1f83bd;
    --brand-deep: #0677ba;
    --card-white: #ffffff;
    --card-dark: #252525;
    --ink: #4a4a4a;
    --ink-strong: #3d3d3d;
    --pipe-pale: #e8f1f8;
    --pipe-mid: #cadeef;
    --back-text: #d6d6d6;
    --icon-blue: #7badd7;
  }
  * { box-sizing: border-box; margin: 0; padding: 0; }
  html, body { width: 1188px; height: 1200px; overflow: hidden; }
  body { background: var(--backdrop); position: relative; font-family: "Roboto", Arial, sans-serif; }

  .card { position: absolute; left: 245px; width: 696px; height: 386px; overflow: hidden; }
  .card-front { top: 159px; background: var(--card-white); }
  .card-back { top: 627px; background: var(--card-dark); }

  .brand-name {
    font-family: "Montserrat", Arial, sans-serif;
    font-weight: 700;
    color: var(--brand-blue);
    white-space: nowrap;
  }
  .brand-dot { position: absolute; border-radius: 50%; background: var(--brand-blue); }

  .front-brand-dot { left: 112px; top: 40px; width: 64px; height: 64px; }
  .front-brand { position: absolute; left: 52px; top: 126px; font-size: 23px; letter-spacing: 0.2px; }

  .accent-tab { position: absolute; left: 0; top: 177px; width: 16px; height: 39px; background: var(--brand-blue); }
  .person-name { position: absolute; left: 53px; top: 174px; font-family: "Montserrat", Arial, sans-serif; font-weight: 700; font-size: 20px; color: var(--brand-blue); }
  .person-title { position: absolute; left: 53px; top: 197px; font-weight: 500; font-size: 18px; color: var(--ink-strong); }

  .address { position: absolute; left: 52px; top: 227px; font-size: 19px; line-height: 24px; color: var(--ink); }
  .contact-list { position: absolute; left: 52px; top: 277px; list-style: none; }
  .contact-list li { display: flex; align-items: center; height: 26px; font-size: 19px; color: var(--ink); }
  .contact-list svg { width: 19px; height: 19px; margin-right: 8px; flex: none; }

  .pipe-art {
    position: absolute; left: 435px; top: 12px; width: 261px; height: 362px;
    background: linear-gradient(160deg, var(--pipe-pale) 0%, #f3f6f8 55%, var(--pipe-mid) 100%);
    border-radius: 60px 0 0 60px;
  }

  .back-brand-dot { left: 318px; top: 92px; width: 60px; height: 60px; }
  .back-brand { position: absolute; left: 0; width: 100%; top: 226px; text-align: center; font-size: 37px; letter-spacing: 0.5px; }
  .features { position: absolute; left: 0; width: 100%; top: 313px; text-align: center; }
  .feature-row { display: flex; justify-content: center; gap: 10px; height: 20px; align-items: center; font-family: "Montserrat", Arial, sans-serif; font-size: 12.5px; color: var(--back-text); }
  .feature { display: flex; align-items: center; gap: 5px; }
  .feature svg { width: 14px; height: 14px; flex: none; }
</style>
</head>
<body>
  <section class="card card-front">
    <span class="brand-dot front-brand-dot"></span>
    <div class="brand-name front-brand">BRIXEN TAPLOR</div>

    <span class="accent-tab"></span>
    <div class="person-name">MARCUS ELLERY</div>
    <div class="person-title">Managing Director</div>

    <p class="address">4180 Harbor Crest Drive<br>Dayton, OH 45402</p>

    <ul class="contact-list">
      <li>
        <svg viewBox="0 0 24 24"><path fill="#1f83bd" d="M6.6 10.8a15.1 15.1 0 0 0 6.6 6.6l2.2-2.2c.3-.3.7-.4 1-.2 1.1.4 2.3.6 3.6.6.6 0 1 .4 1 1V20c0 .6-.4 1-1 1A17 17 0 0 1 3 4c0-.6.4-1 1-1h3.5c.6 0 1 .4 1 1 0 1.3.2 2.5.6 3.6.1.3 0 .7-.2 1z"/></svg>
        +740 555 0184
      </li>
      <li>
        <svg viewBox="0 0 24 24"><rect x="2" y="5" width="20" height="14" fill="none" stroke="#1f83bd" stroke-width="2"/><path d="M2 5l10 8 10-8M2 19l7-7M22 19l-7-7" fill="none" stroke="#1f83bd" stroke-width="1.6"/></svg>
        me@bt204.com
      </li>
      <li>
        <svg viewBox="0 0 24 24"><circle cx="12" cy="12" r="9.5" fill="none" stroke="#1f83bd" stroke-width="1.8"/><path d="M4 9c3 1 5 0 7 2s0 4 2 6M14 3c-1 3 1 4 3 4s3 2 4 3" fill="none" stroke="#1f83bd" stroke-width="1.5"/></svg>
        www.brixentaplorllc.com
      </li>
    </ul>

    <div class="pipe-art" role="img" aria-label="Illustration of pale grey plumbing pipes with a red valve and dripping blue water drops"></div>
  </section>

  <section class="card card-back">
    <span class="brand-dot back-brand-dot"></span>
    <div class="brand-name back-brand">BRIXEN TAPLOR</div>

    <div class="features">
      <div class="feature-row">
        <span class="feature">
          <svg viewBox="0 0 16 16"><circle cx="8" cy="8" r="6.5" fill="none" stroke="#7badd7" stroke-width="1.2"/><text x="8" y="11.5" text-anchor="middle" font-size="9" fill="#7badd7" font-family="Arial, sans-serif">$</text></svg>
          Cost Efficient
        </span>
        <span class="feature">
          <svg viewBox="0 0 16 16"><path d="M8 2l6 10H2z" fill="none" stroke="#7badd7" stroke-width="1.2"/></svg>
          Environmentally Friendly
        </span>
      </div>
      <div class="feature-row">
        <span class="feature">
          <svg viewBox="0 0 16 16"><path d="M5 1h6M6 1v12a2 2 0 0 0 4 0V1" fill="none" stroke="#7badd7" stroke-width="1.2"/></svg>
          Thorough Testing
        </span>
        <span class="feature">
          <svg viewBox="0 0 16 16"><rect x="1.5" y="4" width="13" height="9" fill="none" stroke="#7badd7" stroke-width="1.2"/><path d="M5 4v9M8 4v9M11 4v9" stroke="#7badd7" stroke-width="1"/></svg>
          Variation Testing
        </span>
        <span class="feature">
          <svg viewBox="0 0 16 16"><rect x="3" y="2.5" width="10" height="12" rx="1" fill="none" stroke="#7badd7" stroke-width="1.2"/><path d="M6 2.5h4v2H6zM5.5 8h5M5.5 11h5" fill="none" stroke="#7badd7" stroke-width="1"/></svg>
          Requirement Driven
        </span>
      </div>
    </div>
  </section>
</body>
</html>
```